Business card

would like a double sided business card made up with my logos provided.
Prefer card to have black background and to use the black logos, with matching blue writing for the text.
One side to just be the logo, (Try to use both the black logos)
the other side to have the logo and also my credentials/business information.

Covering all aspects of Carpentry and Building Services

Marcus Tolvey
Qualified Carpenter
Mob: 0417263948
Email: rkt.joinery@mailbright.com
ABN: 47 615 209 834

Industry/Entity Type

Business

Contact Information for Business Card

Marcus Tolvey
Qualified Carpenter
Mob: 0417263948
ABN: 47 615 209 834

Requirements
Must have
• Please try to use both the black logos and incorporate into the card.

```html
<!DOCTYPE html>
<html lang="en">
<head>
<meta charset="utf-8">
<title>RKT Joinery – Business Card</title>
<link rel="stylesheet" href="https://fonts.googleapis.com/css2?family=Montserrat:wght@400;700&family=Arimo:wght@400&display=swap">
<style>
  :root {
    --backdrop: #2b2b2b;
    --card-black: #050505;
    --white: #ffffff;
    --blue: #1e88d2;
    --faint: #1a1a1a;
  }
  html, body {
    margin: 0;
    width: 1200px;
    height: 621px;
    overflow: hidden;
    background: var(--backdrop);
  }
  .canvas {
    position: relative;
    width: 1200px;
    height: 621px;
  }
  .card {
    position: absolute;
    top: 166px;
    width: 505px;
    height: 287px;
    background: var(--card-black);
    overflow: hidden;
    font-family: "Arimo", Arial, sans-serif;
  }
  .card--front { left: 60px; }
  .card--back { left: 628px; }

  /* Front */
  .front-watermark {
    position: absolute;
    left: 0; right: 0;
    top: 40px;
    text-align: center;
    font-family: "Montserrat", sans-serif;
    font-weight: 700;
    font-size: 150px;
    line-height: 1;
    color: var(--faint);
  }
  .front-brand {
    position: absolute;
    left: 0; right: 0;
    top: 108px;
    text-align: center;
  }
  .brand-name {
    font-family: "Montserrat", sans-serif;
    font-weight: 400;
    color: var(--white);
    font-size: 38px;
    line-height: 1;
    letter-spacing: 1px;
  }
  .brand-tagline {
    font-family: "Montserrat", sans-serif;
    font-weight: 400;
    color: var(--blue);
    font-size: 10px;
    letter-spacing: 3.4px;
    margin-top: 4px;
  }
  .front-band {
    position: absolute;
    left: 0; right: 0; bottom: 0;
    height: 38px;
    background: var(--white);
    color: var(--blue);
    font-size: 14px;
    display: flex;
    align-items: center;
    justify-content: center;
  }

  /* Back */
  .back-brand {
    position: absolute;
    left: 26px;
    top: 46px;
  }
  .back-brand .brand-mark {
    font-family: "Montserrat", sans-serif;
    font-weight: 700;
    font-size: 64px;
    line-height: 1;
    color: var(--white);
    letter-spacing: 1px;
  }
  .back-brand .brand-name {
    font-size: 19px;
    letter-spacing: 5.5px;
    margin-top: 8px;
  }
  .back-brand .brand-tagline {
    font-size: 10px;
    letter-spacing: 1.6px;
    margin-top: 3px;
  }
  .holder {
    position: absolute;
    right: 21px;
    top: 52px;
    text-align: right;
  }
  .holder-name { color: var(--white); font-size: 18px; }
  .holder-role { color: var(--blue); font-size: 12.5px; margin-top: 2px; }
  .waves { position: absolute; left: 0; top: 0; }
  .abn {
    position: absolute;
    right: 21px;
    top: 195px;
    color: var(--blue);
    font-size: 13.5px;
  }
  .contact {
    position: absolute;
    right: 21px;
    top: 233px;
    text-align: right;
    font-size: 13px;
    color: var(--card-black);
  }
  .contact-line {
    display: flex;
    align-items: center;
    justify-content: flex-end;
    gap: 9px;
    height: 17px;
  }
  .contact-line svg { width: 11px; height: 11px; }
</style>
</head>
<body>
<div class="canvas">

  <section class="card card--front">
    <div class="front-watermark" aria-hidden="true">RKT</div>
    <div class="front-brand">
      <div class="brand-name">RKT JOINERY</div>
      <div class="brand-tagline">CARPENTERS AND BUILDERS</div>
    </div>
    <div class="front-band">Covering all aspects of Carpentry and Building Services</div>
  </section>

  <section class="card card--back">
    <svg class="waves" width="505" height="287" viewBox="0 0 505 287" aria-hidden="true">
      <path d="M0,287 L0,233 C110,262 210,250 310,188 C390,140 440,128 505,136 L505,287 Z" fill="var(--white)"/>
      <path d="M0,238 C120,268 230,250 320,196 C395,150 440,140 505,144" fill="none" stroke="var(--card-black)" stroke-width="7"/>
      <path d="M0,206 C80,232 170,222 242,170 C170,212 80,214 0,190 Z" fill="var(--blue)"/>
      <path d="M0,228 C90,252 190,238 280,186" fill="none" stroke="var(--card-black)" stroke-width="9"/>
    </svg>
    <div class="back-brand">
      <div class="brand-mark">RKT</div>
      <div class="brand-name">JOINERY</div>
      <div class="brand-tagline">CARPENTERS AND BUILDERS</div>
    </div>
    <div class="holder">
      <div class="holder-name">Marcus Tolvey</div>
      <div class="holder-role">Qualified Carpenter</div>
    </div>
    <div class="abn">ABN: 47 615 209 834</div>
    <div class="contact">
      <div class="contact-line">0417263948
        <svg viewBox="0 0 11 11" aria-label="Mobile"><rect x="2" y="0.5" width="7" height="10" rx="1.5" fill="none" stroke="var(--blue)" stroke-width="1.3"/><rect x="4.3" y="8" width="2.4" height="1" fill="var(--blue)"/></svg>
      </div>
      <div class="contact-line">rkt.joinery@mailbright.com
        <svg viewBox="0 0 11 11" aria-label="Email"><rect x="0" y="2" width="11" height="7.5" fill="var(--blue)"/><path d="M0,2 L5.5,6.5 L11,2" fill="none" stroke="var(--white)" stroke-width="1"/></svg>
      </div>
    </div>
  </section>

</div>
</body>
</html>
```